Need Flyer for Our Real estate Agency

Need to run General Campaign for our agency with Start of New Year as our theme ..Must have an agent's picture on the DL..
Address:
9 / 386Barwin rd, Merrivale VIC 3091
Ph:03 9142 7305
email:info@koridanrealestate.example.au
www.koridanrealestate.example.au
Something like as attached picture..
Target Market(s)
Home Buyers
Industry/Entity Type
Real Estate Agent
Requirements
Must have
- Our Logo Colours

```html
<!DOCTYPE html>
<html lang="en">
<head>
<meta charset="utf-8">
<title>Koridan Real Estate – DL Flyer Options</title>
<link href="https://fonts.googleapis.com/css2?family=Cinzel:wght@400;500&family=Archivo:wght@700&display=swap" rel="stylesheet">
<style>
  :root {
    --navy: #0e1f55;
    --crimson: #6e1620;
    --white: #ffffff;
    --ink: #111111;
    --serif: "Cinzel", "Times New Roman", serif;
    --label: "Archivo", Arial, sans-serif;
  }
  html, body { margin: 0; padding: 0; overflow: hidden; background: var(--white); }
  .canvas { position: relative; width: 1106px; height: 1200px; overflow: hidden; }
  .flyer { position: absolute; left: 0; width: 1106px; background: var(--navy); overflow: hidden; }
  .flyer--one { top: 0; height: 564px; }
  .flyer--two { top: 634px; height: 566px; }
  .flyer__shade { position: absolute; inset: 0; }
  .flyer__band { position: absolute; left: 0; top: 482px; width: 1106px; height: 82px; background: var(--crimson); }
  .flyer__side-block { position: absolute; left: 845px; top: 0; width: 261px; height: 566px; background: var(--crimson); }
  .headline {
    position: absolute; left: 67px; margin: 0; white-space: nowrap;
    font-family: var(--serif); font-weight: 400; font-size: 32px; line-height: 42px;
    color: var(--white); letter-spacing: 0.3px;
  }
  .flyer--one .headline { top: 108px; }
  .flyer--two .headline { top: 118px; }
  .subline {
    position: absolute; left: 67px; margin: 0; white-space: nowrap;
    font-family: var(--serif); font-size: 20px; line-height: 27px; color: var(--white);
  }
  .flyer--one .subline { top: 212px; }
  .flyer--two .subline { top: 222px; }
  .brand { position: absolute; left: 70px; width: 152px; text-align: center; color: var(--white); font-family: var(--serif); font-weight: 400; }
  .brand__square { display: block; width: 26px; height: 26px; margin: 0 auto 14px; border: 2px solid var(--white); box-sizing: border-box; }
  .brand__name { font-size: 27px; letter-spacing: 1px; line-height: 1; }
  .flyer--one .brand { top: 380px; }
  .flyer--two .brand { top: 428px; }
  .contact { position: absolute; margin: 0; font-family: var(--serif); color: var(--white); white-space: nowrap; }
  .contact--band { left: 74px; top: 498px; font-size: 13.5px; line-height: 22px; }
  .contact--band .sep { margin: 0 8px; }
  .contact--stack { left: 253px; top: 406px; font-size: 15px; line-height: 26.5px; }
  .contact-rule { position: absolute; left: 240px; top: 412px; width: 1px; height: 90px; background: rgba(255,255,255,0.35); }
  .agent-frame { position: absolute; left: 622px; width: 432px; height: 459px; background: var(--crimson); box-sizing: border-box; padding: 4px; }
  .flyer--one .agent-frame { top: 50px; }
  .flyer--two .agent-frame { top: 58px; height: 460px; }
  .agent-photo { width: 100%; height: 100%; }
  .agent-photo--cool { background: linear-gradient(160deg, #f4f6ff 0%, #c9d2f2 40%, #6e7fbf 70%, #1c2a66 100%); }
  .agent-photo--warm { background: linear-gradient(160deg, #fff2f5 0%, #f0c4d0 40%, #a95a72 70%, #4a1626 100%); }
  .options { position: absolute; left: 0; top: 564px; width: 1106px; height: 70px; background: var(--white); }
  .option { position: absolute; font-family: var(--label); font-weight: 700; font-size: 17px; color: var(--ink); }
  .option--one { left: 355px; top: 22px; }
  .option--two { left: 534px; top: 22px; }
  .option-arrow { position: absolute; }
</style>
</head>
<body>
<div class="canvas">

  <section class="flyer flyer--one">
    <svg class="flyer__shade" width="1106" height="564" aria-hidden="true">
      <defs>
        <linearGradient id="shadeOne" x1="1" y1="0" x2="0" y2="1">
          <stop offset="0" stop-color="#071233" stop-opacity="0.85"/>
          <stop offset="1" stop-color="#0e1f55" stop-opacity="0"/>
        </linearGradient>
      </defs>
      <polygon points="622,50 622,509 1054,509 1054,564 300,564 300,372" fill="url(#shadeOne)"/>
    </svg>
    <div class="flyer__band"></div>
    <svg class="flyer__shade" width="1106" height="564" aria-hidden="true">
      <polygon points="622,509 1054,509 954,564 560,564" fill="#3a0b12" opacity="0.6"/>
    </svg>
    <h1 class="headline">Curious to know what<br>your home is worth?</h1>
    <p class="subline">Proin gravida nibh vel velit auctor<br>aliquet. Class aptent taciti</p>
    <div class="brand"><span class="brand__square"></span><span class="brand__name">KORIDAN</span></div>
    <p class="contact contact--band">9 / 386Barwin rd, Merrivale VIC 3091<span class="sep">|</span>Ph:03 9142 7305<br>email:info@koridanrealestate.example.au<span class="sep">|</span>www.koridanrealestate.example.au</p>
    <div class="agent-frame"><div class="agent-photo agent-photo--cool" role="img" aria-label="Portrait of the agent in a suit, arms crossed, by bright office windows, blue tint"></div></div>
  </section>

  <div class="options">
    <svg class="option-arrow" style="left:354px;top:6px" width="82" height="16" aria-hidden="true"><polygon points="0,16 41,0 82,16" fill="#000"/></svg>
    <span class="option option--one">OPTION 1</span>
    <span class="option option--two">OPTION 2</span>
    <svg class="option-arrow" style="left:534px;top:48px" width="82" height="16" aria-hidden="true"><polygon points="0,0 82,0 41,16" fill="#000"/></svg>
  </div>

  <section class="flyer flyer--two">
    <div class="flyer__side-block"></div>
    <svg class="flyer__shade" width="1106" height="566" aria-hidden="true">
      <defs>
        <linearGradient id="shadeTwo" x1="1" y1="0" x2="0" y2="1">
          <stop offset="0" stop-color="#071233" stop-opacity="0.85"/>
          <stop offset="1" stop-color="#0e1f55" stop-opacity="0"/>
        </linearGradient>
      </defs>
      <polygon points="622,58 622,518 845,518 845,566 260,566 260,420" fill="url(#shadeTwo)"/>
    </svg>
    <h1 class="headline">Curious to know what<br>your home is worth?</h1>
    <p class="subline">Proin gravida nibh vel velit auctor<br>aliquet. Class aptent taciti</p>
    <div class="brand"><span class="brand__square"></span><span class="brand__name">KORIDAN</span></div>
    <div class="contact-rule"></div>
    <p class="contact contact--stack">9 / 386Barwin rd, Merrivale VIC 3091<br>Ph:03 9142 7305<br>email:info@koridanrealestate.example.au<br>www.koridanrealestate.example.au</p>
    <div class="agent-frame"><div class="agent-photo agent-photo--warm" role="img" aria-label="Portrait of the agent in a suit, arms crossed, by bright office windows, crimson tint"></div></div>
  </section>

</div>
</body>
</html>
```